Web Design Project

blaze guard safety & solutions needs a new web design to go with its new logo design

we provide services such as instillation of fire sprinklers, fire hydrants , fire hose reels as well as fire extinguishers and fire blankets.

we can service these as well and also do the preventitave maintaince of these too.

we can do flow testing of sprinklers,hydrants & hosereels and test back flow prevention devices as well

old page is bgss-example.com.au

Industry/Entity Type

Defence

```html
<!DOCTYPE html>
<html lang="en">
<head>
<meta charset="utf-8">
<title>Blaze Guard Safety &amp; Solutions</title>
<link rel="stylesheet" href="https://fonts.googleapis.com/css2?family=Arimo:ital,wght@0,400;0,700;1,400;1,700&display=swap">
<style>
:root{
  --rust:#b5461c;
  --charcoal:#262626;
  --ink:#2a2a2a;
  --page:#ececec;
  --white:#ffffff;
  --text:#8a8a8a;
  --link:#d4531e;
  --frame:#dcdcdc;
}
*{margin:0;padding:0;box-sizing:border-box}
html,body{width:876px;height:1200px;overflow:hidden}
body{font-family:"Arimo",Arial,sans-serif;background:var(--page);position:relative;color:var(--ink)}
.top-band{position:absolute;left:0;top:0;width:876px;height:426px;background:var(--rust)}
.bottom-bar{position:absolute;left:0;top:1160px;width:876px;height:40px;background:var(--charcoal)}
.copyright{position:absolute;right:28px;top:1174px;color:var(--white);font-size:12px}
.sheet{position:absolute;left:25px;top:30px;width:823px;height:1080px;background:var(--white)}
.abs{position:absolute}

.brand{left:30px;top:32px;width:400px}
.brand-row{display:flex;align-items:center;gap:12px}
.brand-square{width:44px;height:44px;background:var(--rust);flex:none}
.brand-name{font-size:22px;font-weight:700;color:var(--ink);line-height:24px}
.brand-tag{margin-top:12px;font-size:10px;font-weight:700;color:var(--text);letter-spacing:.5px}

.main-nav{left:13px;top:125px;display:flex;gap:2px}
.main-nav a{display:flex;align-items:center;justify-content:center;width:113px;height:42px;background:var(--charcoal);color:var(--white);text-decoration:none;font-size:13px}
.main-nav a.is-active{background:var(--rust)}
.main-nav a.small{font-size:10.5px}

.hero{left:12px;top:174px;width:799px;height:283px;background:linear-gradient(180deg,#8f8f8c 0%,#6d5a50 45%,#4a3a30 100%)}
.hero-quote{left:35px;top:74px;color:var(--white);font-style:italic;font-size:27px}

.call-box{left:13px;top:487px;width:188px;height:101px;background:var(--rust);color:var(--white);padding-top:25px}
.call-box .l1{font-size:14px;padding-left:8px}
.call-box .l2{font-size:18px;text-align:right;padding-right:10px}
.call-box .num{font-size:26px;font-weight:700;margin-top:4px;text-align:center}

.side-head{left:13px;width:188px;height:34px;background:var(--charcoal);color:var(--white);font-size:23px;padding-left:6px;line-height:34px}
.contact-info{left:16px;top:642px;font-size:10.5px;line-height:13px;color:var(--ink)}
.contact-info p{margin-bottom:10px}
.contact-info span{color:var(--link)}

.quote-btn{left:13px;top:748px;width:188px;height:86px;background:var(--rust);border-radius:8px;color:var(--white);font-weight:700;font-style:italic;font-size:24px;line-height:25px;text-align:right;padding:20px 10px 0 0}

.service-list{left:29px;top:884px;list-style:none;width:138px}
.service-list li{font-size:11.5px;color:var(--text);height:24px;line-height:22px;border-bottom:1px solid var(--ink);padding-left:14px;position:relative}
.service-list li::before{content:"";position:absolute;left:1px;top:8px;width:7px;height:7px;border-radius:50%;background:var(--rust)}

.welcome{left:223px;top:468px;font-size:29px;font-weight:400;color:var(--ink);border-bottom:2px solid var(--ink);padding-bottom:1px}
.intro{left:223px;top:508px;width:590px;font-size:11px;line-height:13.5px;color:var(--text)}
.intro p{margin-bottom:14px}

.card{top:739px;width:195px}
.card-photo{width:195px;height:146px;border:4px solid var(--frame)}
.card h3{font-weight:400;font-size:24px;line-height:24px;margin-top:8px;padding-left:4px}
.card h3 span{display:block;font-size:18px;line-height:20px;padding-left:24px}
.card h3 sub{font-size:15px;line-height:0;vertical-align:-4px}
.card p{font-size:9px;line-height:11px;color:var(--text);margin-top:6px;padding-left:6px}
.more{display:inline-block;margin-top:6px;background:var(--charcoal);color:var(--white);font-size:18px;padding:3px 14px;text-decoration:none}

.foot-nav{left:38px;top:1116px;font-size:11.5px;color:var(--ink);word-spacing:1px}
.social{left:732px;top:1116px;display:flex;gap:8px}
.social span{width:28px;height:28px;border-radius:4px;background:#b9b9b9;display:block}
</style>
</head>
<body>
<div class="top-band"></div>
<div class="sheet">
  <div class="abs brand">
    <div class="brand-row"><span class="brand-square"></span><span class="brand-name">Blaze Guard Safety &amp; Solutions</span></div>
    <div class="brand-tag">YOUR BEST DEFENCE AGAINST FIRE</div>
  </div>

  <nav class="abs main-nav">
    <a class="is-active">HOME</a><a>AOBUT US</a><a>TESTING</a><a>PRODUCTS</a><a>FAQ'S</a><a class="small">REQUEST A QUOTE</a><a>CONTACT US</a>
  </nav>

  <div class="abs hero" role="img" aria-label="Photo of firefighters in gear posing in front of a fire engine at a fire station">
    <div class="abs hero-quote">“Your best defence against fire”</div>
  </div>

  <div class="abs call-box">
    <div class="l1">Call for Fire Information</div>
    <div class="l2">24 hours a day</div>
    <div class="num">000 000 0000</div>
  </div>

  <div class="abs side-head" style="top:595px">Contact Us</div>
  <div class="abs contact-info">
    <p>Mail: P.O Box 1234,<br>Seaview, NSW 2000</p>
    <p>Email: <span>info@bgss-example.com.au</span></p>
    <p>Mobile 0491570156</p>
    <p>Accounts: <span>accounts@bgss-example.com.au</span></p>
  </div>

  <div class="abs quote-btn">Request<br>a Quote</div>

  <div class="abs side-head" style="top:842px">Our Services</div>
  <ul class="abs service-list">
    <li>Fire Extinguishers</li><li>Fire Engines</li><li>Sprinklers</li><li>Fire Extinguishers</li><li>Fire Engines</li><li>Sprinklers</li>
  </ul>

  <h1 class="abs welcome">Welcome to BGSS</h1>
  <div class="abs intro">
    <p>At blaze guard we believe that no matter how large or small your business is we can help you with the design, installation and the maintenance of your system to the standard which it was designed to.</p>
    <p>Blaze Guard is a fire protection company situated on the Central Coast of NSW and is currently servicing the Sydney,Central Coast and Hunter areas, We are always looking for new clients who are not happy with there current service providers and are looking for a Competitive priced alternative.</p>
    <p>Blaze guard will come to your site and assess your fire service assets and provide a full quotation on a 12 month service contract.</p>
    <p>Blaze Guard can also supply quotations for any alterations to your Sprinklers,Hydrants &amp; Hose reel systems along with your fire detection and emergency lighting.</p>
    <p>Blaze guard is a owner operated business, so our reputation is our guarantee to do the best job we possibily can.</p>
  </div>

  <div class="abs card" style="left:211px">
    <div class="card-photo" role="img" aria-label="Photo of an open fire hydrant spraying water across grass" style="background:linear-gradient(180deg,#6f7f6a,#c9d0cc 60%,#7f8a5a)"></div>
    <h3>Fire Hydrants<span>for General Fires</span></h3>
    <p>Praesent tibulum molestie lacueno mera yhe ndrerit mauris ketyade. Phasellus porta. Fusce suscipit vari uslasera. Cum soci iseras natoque nertyades.........</p>
    <a class="more">More</a>
  </div>
  <div class="abs card" style="left:415px">
    <div class="card-photo" role="img" aria-label="Photo of firefighters spraying foam on an oil fire" style="background:linear-gradient(180deg,#3c4a3a,#8a8f88 55%,#d8dcd8)"></div>
    <h3>Foam type<span>for Oil Fires</span></h3>
    <p>Praesent tibulum molestie lacueno mera yhe ndrerit mauris ketyade. Phasellus porta. Fusce suscipit vari uslasera. Cum soci iseras natoque nertyades.........</p>
    <a class="more">More</a>
  </div>
  <div class="abs card" style="left:618px">
    <div class="card-photo" role="img" aria-label="Photo of a hand holding a red fire extinguisher" style="background:linear-gradient(135deg,#f3f3f3 30%,#d9352e 75%,#b01e1e)"></div>
    <h3>CO<sub>2</sub> type<span>for Electrical Fires</span></h3>
    <p>Praesent tibulum molestie lacueno mera yhe ndrerit mauris ketyade. Phasellus porta. Fusce suscipit vari uslasera. Cum soci iseras natoque nertyades.........</p>
    <a class="more">More</a>
  </div>
</div>

<div class="abs foot-nav">Home About Us Testing Products&nbsp; FAQ's Request a Quote Contact Us</div>
<div class="abs social" aria-label="Social links"><span></span><span></span><span></span></div>
<div class="bottom-bar"></div>
<div class="copyright">Copyright@2011</div>
</body>
</html>
```